Plastic Business Card for Bookkeeper

We are looking for a simple professional business card design to use for printing on thin frosted plastic (see-through) card stock. Logo and brand guideline documents are attached as well as a photo of our old business card, and another business card example that we like.

Target Market(s)

Small Business

Industry/Entity Type

Bookkeeper

Contact Information for Business Card

Harriet Olsen CPA
Chief Executive Bookkeeper
T. 03 5926 4417
M. 0438 761 205
E. harriet@pinecrestledger.com
W. www.pinecrestledger.com

Font styles to use
Sans Serif

Colors
6b449b
00a990

Requirements
Must have
• Stick with logo colors. Writing should be clear and easy to read and not too cramped together.
Nice to have
• Tag line for back of the card - 'Not your ordinary Bookkeeper'

```html
<!DOCTYPE html>
<html lang="en">
<head>
<meta charset="utf-8">
<title>Pinecrest Ledger – Business Card</title>
<link rel="stylesheet" href="https://fonts.googleapis.com/css2?family=Exo+2:wght@600&family=Roboto:wght@400;500&family=Patrick+Hand&display=swap">
<style>
  :root {
    --backdrop: #2b2b2e;
    --card-white: #f4f4f6;
    --brand-purple: #6a2cb0;
    --brand-purple-deep: #5a2399;
    --brand-teal: #16908f;
    --ink: #1c1c1f;
    --tagline: #cdb8ea;
  }
  * { box-sizing: border-box; margin: 0; padding: 0; }
  html, body { width: 1200px; height: 800px; overflow: hidden; }
  body {
    background: var(--backdrop);
    position: relative;
    font-family: "Roboto", Arial, sans-serif;
  }
  .card {
    position: absolute;
    top: 245px;
    width: 540px;
    height: 310px;
    border-radius: 20px;
    overflow: hidden;
    background: var(--card-white);
    box-shadow: 0 14px 30px rgba(0,0,0,.45);
  }
  .card-front { left: 40px; }
  .card-back { left: 620px; }

  .front-band {
    position: absolute; left: 0; right: 0; bottom: 0; height: 96px;
    background: linear-gradient(180deg, var(--brand-teal) 0 5px, var(--card-white) 5px 14px, var(--brand-purple) 14px, var(--brand-purple-deep) 100%);
  }
  .back-panel {
    position: absolute; left: 0; top: 0; bottom: 0; width: 300px;
    background: linear-gradient(90deg, var(--brand-purple-deep), var(--brand-purple) 92%, var(--card-white) 92% 96%, var(--brand-teal) 96%);
  }

  .holder-name {
    position: absolute; left: 32px; top: 26px;
    font-family: "Exo 2", Arial, sans-serif; font-weight: 600;
    font-size: 25px; color: var(--brand-purple);
  }
  .holder-title {
    position: absolute; left: 32px; top: 60px;
    font-size: 15px; color: var(--ink);
  }
  .contact-list {
    position: absolute; left: 32px; top: 92px;
    list-style: none;
  }
  .contact-list li {
    display: flex; align-items: center; gap: 12px;
    height: 22px; font-size: 16px; color: var(--ink);
  }
  .contact-icon { width: 13px; height: 13px; fill: var(--brand-purple); flex: none; }

  .wordmark {
    position: absolute; right: 30px; bottom: 28px;
    display: flex; align-items: center; gap: 12px;
  }
  .wordmark-dot { width: 26px; height: 26px; border-radius: 50%; background: #fff; }
  .wordmark-name {
    font-weight: 500; font-size: 24px; letter-spacing: 1px;
    color: #fff; text-transform: uppercase;
  }

  .tagline {
    position: absolute; left: 70px; top: 60px;
    font-family: "Patrick Hand", "Comic Sans MS", cursive;
    font-size: 27px; line-height: 1.15; color: var(--tagline);
  }
</style>
</head>
<body>

<section class="card card-front" aria-label="Business card front">
  <div class="front-band" role="img" aria-label="Purple band with teal accent line"></div>

  <h1 class="holder-name">Harriet Olsen CPA</h1>
  <p class="holder-title">Chief Executive Bookkeeper</p>

  <ul class="contact-list">
    <li><svg class="contact-icon" viewBox="0 0 16 16" aria-hidden="true"><path d="M3 1h3l1.5 4-2 1.2a9 9 0 0 0 4.3 4.3L11 8.5l4 1.5v3a2 2 0 0 1-2 2A12 12 0 0 1 1 3a2 2 0 0 1 2-2z"/></svg>03 5926 4417</li>
    <li><svg class="contact-icon" viewBox="0 0 16 16" aria-hidden="true"><path d="M4 0h8a1 1 0 0 1 1 1v14a1 1 0 0 1-1 1H4a1 1 0 0 1-1-1V1a1 1 0 0 1 1-1zm1 2v10h6V2zm3 11a1 1 0 1 0 0 2 1 1 0 0 0 0-2z"/></svg>0438 761 205</li>
    <li><svg class="contact-icon" viewBox="0 0 16 16" aria-hidden="true"><path d="M0 3h16v10H0zm1.5 1.5L8 9l6.5-4.5V4h-13z"/></svg>harriet@pinecrestledger.com</li>
    <li><svg class="contact-icon" viewBox="0 0 16 16" aria-hidden="true"><path d="M8 0a8 8 0 1 0 0 16A8 8 0 0 0 8 0zm0 2c.8 1 1.4 3 1.5 5h-3C6.6 5 7.2 3 8 2zM2.1 9H5a12 12 0 0 0 1 4.8A6 6 0 0 1 2.1 9zm0-2A6 6 0 0 1 6 2.2 12 12 0 0 0 5 7zm11.8 0h-2.9a12 12 0 0 0-1-4.8A6 6 0 0 1 13.9 7zM8 14c-.8-1-1.4-3-1.5-5h3c-.1 2-.7 4-1.5 5zm2-.2a12 12 0 0 0 1-4.8h2.9a6 6 0 0 1-3.9 4.8z"/></svg>www.pinecrestledger.com</li>
  </ul>

  <div class="wordmark">
    <span class="wordmark-dot"></span>
    <span class="wordmark-name">Pinecrest Ledger</span>
  </div>
</section>

<section class="card card-back" aria-label="Business card back">
  <div class="back-panel" role="img" aria-label="Purple panel with teal accent edge"></div>
  <p class="tagline">Not your<br>ordinary<br>Bookkeeper</p>
</section>

</body>
</html>
```